Book Cover Design Project - "Cue The Panic"

"Cue the panic - making videos to boost business" is a business book that outlines what you need to know if you are planning to make videos for business communications.
The intended audience for the book is small to medium business owners. These are people who are keen to learn what they should know to do it themselves.
The cover needs to have a clear design that works as a thumbnail as well as full size.
Feel free to have some fun with it. It doesn't have to be all serious. Although this is a business book many people are afraid and don't know where to start with video production.
My company logo uses red, black, grey and white - www.velkarmedia.com.au . The logo has been uploaded.
It is not critical to use those elements, however if it can be incorporated into the design that's good too. The priority however is having a design that is eye catching.
The book will about 200 pages long. The back will include an authors photo, so blurb and testimonials- a word doc has been uploaded. It will also include the barcode, ISBN number, and price.
The spine will need to be clear and eyecatching as well.
The design should clearly reveal that this is about video production and provide a feeling of competency and comfort for those who read it.
Updates

The dimensions for the cover should be 12.8cm x 19.8cm.

At this point the spine thickness will be about 1.5cm x 19.8cm high

Please include my name on the front cover of the design:

Brent Malloway

Target Market(s)

The book is targeted to small to medium business owners who want to know how to make videos for their business. They are do it yourself people.

Industry/Entity Type

Business

Requirements
Must have
• Front
Title: Cue the panic
Tagline: Making videos to boost business

I would also like the spine and back cover done as part of the design, however let's get the front done and then the rest can be completed based on the approved design.
Nice to have
• Cue the panic is a play on words in regards to being filmed (shot) and the anxiety people feel about presenting in front of a camera.
One idea I've had (but I'm not attached to it), is to make the markings that are present in a camera's viewfinder to resemble those that are seen through the sights of a gun.
I'm really not attached to it and unless that can be achieved in a playful way, it is probably best to avoid.
Should not have
• Please avoid images of low budget cameras. The impression we want here is that this is professional standard video production advice. (By the way you don't have to have any cameras at all).

Low budget cameras are handycams etc.

```html
<!DOCTYPE html>
<html lang="en">
<head>
<meta charset="utf-8">
<title>Cue The Panic – Making Videos to Boost Business</title>
<link rel="stylesheet" href="https://fonts.googleapis.com/css2?family=Bebas+Neue&family=Open+Sans:wght@400;600&display=swap">
<style>
  :root {
    --cover-black: #050505;
    --signal-red: #e8141b;
    --lens-white: #ffffff;
    --lens-edge: #d9d9d9;
    --ink-black: #111111;
    --ui-white: #f2f2f2;
  }
  html, body {
    margin: 0;
    padding: 0;
    width: 775px;
    height: 1200px;
    overflow: hidden;
    background: var(--cover-black);
  }
  .book-cover {
    position: relative;
    width: 775px;
    height: 1200px;
    background: var(--cover-black);
    overflow: hidden;
    font-family: "Open Sans", Arial, sans-serif;
  }
  .battery-icon {
    position: absolute;
    left: 56px;
    top: 150px;
    width: 58px;
    height: 30px;
  }
  .rec-label {
    position: absolute;
    right: 70px;
    top: 88px;
    margin: 0;
    font-family: "Open Sans", Arial, sans-serif;
    font-weight: 600;
    font-size: 40px;
    letter-spacing: 1px;
    color: var(--signal-red);
  }
  .viewfinder {
    position: absolute;
    left: 88px;
    top: 230px;
    width: 600px;
    height: 600px;
  }
  .viewfinder svg {
    position: absolute;
    inset: 0;
    width: 100%;
    height: 100%;
  }
  .book-title {
    position: absolute;
    inset: 0;
    margin: 0;
    display: flex;
    flex-direction: column;
    align-items: center;
    justify-content: center;
    font-family: "Bebas Neue", Impact, sans-serif;
    font-weight: 400;
    line-height: 0.86;
    text-align: center;
  }
  .book-title span { display: block; }
  .title-line-one { font-size: 132px; color: var(--signal-red); }
  .title-line-two { font-size: 236px; color: var(--signal-red); }
  .title-line-three { font-size: 156px; color: var(--ink-black); }
  .tagline-frame {
    position: absolute;
    left: 44px;
    top: 858px;
    width: 690px;
    height: 120px;
  }
  .tagline-frame svg {
    position: absolute;
    inset: 0;
    width: 100%;
    height: 100%;
  }
  .tagline {
    position: absolute;
    left: 0;
    right: 0;
    top: 40px;
    margin: 0;
    text-align: center;
    font-family: "Open Sans", Arial, sans-serif;
    font-weight: 400;
    font-size: 29px;
    letter-spacing: 2px;
    text-transform: uppercase;
    color: var(--ui-white);
  }
  .author-name {
    position: absolute;
    left: 0;
    right: 0;
    top: 1005px;
    margin: 0;
    text-align: center;
    font-family: "Bebas Neue", Impact, sans-serif;
    font-weight: 400;
    font-size: 104px;
    letter-spacing: 3px;
    color: var(--signal-red);
  }
</style>
</head>
<body>
  <main class="book-cover">
    <svg class="battery-icon" viewBox="0 0 58 30" aria-hidden="true">
      <rect x="1.5" y="1.5" width="51" height="27" rx="2" fill="none" stroke="var(--ui-white)" stroke-width="3"/>
      <rect x="53" y="9" width="4" height="12" fill="var(--ui-white)"/>
      <polygon points="8,6 21,6 16,24 5,24" fill="var(--ui-white)"/>
      <polygon points="24,6 35,6 30,24 19,24" fill="var(--ui-white)"/>
      <polygon points="38,6 48,6 48,24 33,24" fill="var(--ui-white)"/>
    </svg>

    <p class="rec-label">REC</p>

    <section class="viewfinder">
      <svg viewBox="0 0 600 600" aria-hidden="true">
        <defs>
          <radialGradient id="lens-glow" cx="50%" cy="50%" r="50%">
            <stop offset="0%" stop-color="var(--lens-white)"/>
            <stop offset="90%" stop-color="var(--lens-white)"/>
            <stop offset="100%" stop-color="var(--lens-edge)"/>
          </radialGradient>
        </defs>
        <circle cx="300" cy="300" r="298" fill="url(#lens-glow)"/>
        <g stroke="var(--ink-black)" stroke-width="3">
          <line x1="300" y1="-4" x2="300" y2="62"/>
          <line x1="300" y1="538" x2="300" y2="604"/>
          <line x1="-4" y1="300" x2="62" y2="300"/>
          <line x1="538" y1="300" x2="604" y2="300"/>
        </g>
      </svg>
      <h1 class="book-title">
        <span class="title-line-one">Cue</span>
        <span class="title-line-two">The</span>
        <span class="title-line-three">Panic</span>
      </h1>
    </section>

    <section class="tagline-frame">
      <svg viewBox="0 0 690 120" aria-hidden="true">
        <polyline points="22,44 2,44 2,0 22,0" transform="translate(0,20) scale(1,1)" fill="none" stroke="var(--ui-white)" stroke-width="3" />
        <polyline points="10,14 2,14 2,70 " fill="none" stroke="none"/>
        <polyline points="688,78 688,118 668,118" fill="none" stroke="var(--ui-white)" stroke-width="3"/>
        <polyline points="668,60 688,60" fill="none" stroke="var(--ui-white)" stroke-width="3"/>
      </svg>
      <p class="tagline">Making videos to boost business</p>
    </section>

    <p class="author-name">Brent Malloway</p>
  </main>
</body>
</html>
```